Corkmill Cafe' eLiquid Label - retro, trendy design

Need a 1.5"x3" label designed for an eLiquid bottle. I like the distressed retro diner look. Feel free to take creative license on logo, images etc. Attaching a mockup I did just to give you an idea of what look I want - the attached concept has all textual elements required....want retro trendy....hollowell-ish look and personality...warm colors...high contrasts. attached Vesk image is the mockup I want redesigned.

Target Market(s)

eclectic

Industry/Entity Type

Cafe

Font styles to use
Serif
Decorative

Requirements
Must have
• text elements from uploaded sample - 1.5x3 inch high res
Nice to have
• incorporate QN logo somewhere in the design - attached

```html
<!DOCTYPE html>
<html lang="en">
<head>
<meta charset="utf-8">
<title>Corkmill Vapor – eLiquid Label</title>
<link rel="stylesheet" href="https://fonts.googleapis.com/css2?family=Bodoni+Moda:opsz,wght@6..96,600;6..96,700&family=Kaushan+Script&display=swap">
<style>
  :root {
    --page: #f1f2f2;
    --label-bg: #4a2a0b;
    --label-bg-light: #5e3810;
    --label-bg-dark: #3c2108;
    --amber: #e79b1f;
    --amber-soft: #f0ae3a;
    --script: #e3992a;
    --rust: #ab561c;
    --red: #c4291a;
    --skyline-dark: #4a2606;
    --skyline-mid: #c87a14;
    --skyline-light: #f4a827;
  }
  html, body {
    margin: 0;
    width: 1200px;
    height: 849px;
    overflow: hidden;
    background: var(--page);
  }
  .label {
    display: block;
    width: 1200px;
    height: 849px;
    font-family: "Bodoni Moda", "Times New Roman", serif;
    font-weight: 700;
  }
  .label-bg { fill: var(--label-bg); }
  .label-wear { fill: url(#wearTone); }
  .brand-name { fill: var(--rust); font-size: 92px; opacity: .92; }
  .brand-sub { fill: var(--script); font-family: "Kaushan Script", cursive; font-weight: 400; font-size: 84px; }
  .tagline { fill: var(--red); font-size: 23px; }
  .skyline-photo { fill: url(#skylineTone); }
  .skyline-shade { fill: url(#skylineShade); }
  .flavor-ring { fill: none; stroke: var(--rust); stroke-width: 10; opacity: .8; }
  .flavor-name { fill: var(--red); font-family: "Kaushan Script", cursive; font-weight: 400; font-size: 44px; }
  .ingredients { fill: var(--amber); font-size: 17px; }
  .warning { fill: var(--amber); font-size: 13px; }
  .strength-dot { fill: var(--amber); }
  .strength-value { fill: var(--amber); font-size: 27px; }
  .origin { fill: var(--amber); font-size: 16px; }
  .batch-code { fill: var(--amber); font-size: 10px; }
  .web-address { fill: var(--amber-soft); font-size: 31px; }
</style>
</head>
<body>
<svg class="label" viewBox="0 0 1200 849" xmlns="http://www.w3.org/2000/svg">
  <defs>
    <radialGradient id="wearTone" cx="0.45" cy="0.35" r="0.75">
      <stop offset="0" stop-color="var(--label-bg-light)" stop-opacity=".9"/>
      <stop offset="0.6" stop-color="var(--label-bg)" stop-opacity="0"/>
      <stop offset="1" stop-color="var(--label-bg-dark)" stop-opacity=".9"/>
    </radialGradient>
    <linearGradient id="skylineTone" x1="0" y1="0" x2="0" y2="1">
      <stop offset="0" stop-color="var(--skyline-light)"/>
      <stop offset="0.55" stop-color="var(--skyline-mid)"/>
      <stop offset="1" stop-color="var(--skyline-dark)"/>
    </linearGradient>
    <linearGradient id="skylineShade" x1="0" y1="0" x2="1" y2="0">
      <stop offset="0" stop-color="var(--skyline-dark)" stop-opacity=".35"/>
      <stop offset="0.5" stop-color="var(--skyline-dark)" stop-opacity="0"/>
      <stop offset="1" stop-color="var(--skyline-dark)" stop-opacity=".3"/>
    </linearGradient>
  </defs>

  <rect class="label-bg" x="99" y="143" width="996" height="496"/>
  <rect class="label-wear" x="99" y="143" width="996" height="496"/>

  <g class="masthead">
    <text class="brand-name" x="372" y="238" textLength="450" lengthAdjust="spacingAndGlyphs">Corkmill</text>
    <text class="brand-sub" x="505" y="300" textLength="310" lengthAdjust="spacingAndGlyphs">vapor</text>
    <text class="tagline" x="403" y="334" textLength="197" lengthAdjust="spacingAndGlyphs">Ultra Premium</text>
    <text class="tagline" x="648" y="334" textLength="152" lengthAdjust="spacingAndGlyphs">Mod Grease</text>
  </g>

  <g class="skyline" role="img" aria-label="Distressed amber photo of a city skyline with a cable-stayed bridge at dusk">
    <path class="skyline-photo" d="M230 357 H985 V590 H215 V372 Q215 357 230 357 Z"/>
    <path class="skyline-shade" d="M230 357 H985 V590 H215 V372 Q215 357 230 357 Z"/>
  </g>

  <g class="flavor-badge">
    <circle class="flavor-ring" cx="583" cy="468" r="88"/>
    <text class="flavor-name" x="480" y="485" textLength="230" lengthAdjust="spacingAndGlyphs">Citrelle</text>
  </g>

  <text class="ingredients" x="330" y="610" textLength="548" lengthAdjust="spacingAndGlyphs">Vegetable Glycerin, Propylene Glycol, Flavoring, Nicotine</text>

  <text class="warning" transform="translate(134 610) rotate(-90)" textLength="430" lengthAdjust="spacingAndGlyphs">18+, Do Not Drink, Keep Out of reach of Pets and Children</text>

  <g class="strength-scale">
    <circle class="strength-dot" cx="160" cy="567" r="8"/>
    <circle class="strength-dot" cx="160" cy="521" r="8"/>
    <circle class="strength-dot" cx="160" cy="474" r="8"/>
    <circle class="strength-dot" cx="160" cy="419" r="8"/>
    <circle class="strength-dot" cx="160" cy="362" r="8"/>
    <g text-anchor="middle">
      <text class="strength-value" transform="translate(201 567) rotate(-90)">0</text>
      <text class="strength-value" transform="translate(201 521) rotate(-90)">3</text>
      <text class="strength-value" transform="translate(201 474) rotate(-90)">6</text>
      <text class="strength-value" transform="translate(201 419) rotate(-90)">12</text>
      <text class="strength-value" transform="translate(201 362) rotate(-90)">18</text>
    </g>
  </g>

  <text class="origin" transform="translate(1024 490) rotate(-90)" textLength="180" lengthAdjust="spacingAndGlyphs">~&#160;&#160;Made in the U.S.A.</text>
  <text class="batch-code" transform="translate(1021 303) rotate(-90)">CKLB</text>

  <text class="web-address" transform="translate(1064 612) rotate(-90)" textLength="440" lengthAdjust="spacingAndGlyphs">www.corkmillvapor.com</text>
</svg>
</body>
</html>
```